Conference banner for Kestrel training organisation

We empower everyday heroes.
We provide training that empowers individuals to create positive change in themselves, their community, and the world.
We need a large banner design to promote the organisation at conferences and events. We are open to ideas and creativity.
It may involve creatively displaying our logo only, or it may involve our logo and a summary of our products (Kestrel training, Calm Minds Field Care).
Size: 820mm width x 1790mm height
300dpi
Target Market(s)
Educators and frontline health, community, and social workers.
Industry/Entity Type
Training
Colors
Designer to choose colors to be used in the design.

```html
<!DOCTYPE html>
<html lang="en">
<head>
<meta charset="utf-8">
<title>Kestrel Hub – Conference Banner</title>
<link rel="stylesheet" href="https://fonts.googleapis.com/css2?family=Jost:wght@600;700&display=swap">
<style>
  :root {
    --navy: #0e2d4f;
    --headline: #e4e6e9;
    --headline-strong: #ffffff;
    --brand-blue: #2e75bd;
    --brand-blue-deep: #2a6cb3;
    --brand-red: #b84555;
  }
  html, body {
    margin: 0;
    padding: 0;
    width: 1200px;
    height: 2619px;
    overflow: hidden;
    background: var(--navy);
  }
  .banner {
    position: relative;
    width: 1200px;
    height: 2619px;
    background: var(--navy);
    font-family: "Jost", "Futura", sans-serif;
  }
  .tagline {
    position: absolute;
    left: 226px;
    top: 332px;
    margin: 0;
    font-weight: 700;
    font-size: 122px;
    line-height: 157px;
    letter-spacing: -2px;
    text-transform: uppercase;
    color: var(--headline);
  }
  .tagline span { display: block; }
  .tagline .tagline-emphasis { color: var(--headline-strong); }
  .brand-emblem {
    position: absolute;
    left: 250px;
    top: 1340px;
    width: 660px;
    height: 660px;
  }
  .brand-name {
    position: absolute;
    left: 0;
    right: 0;
    top: 2120px;
    margin: 0;
    text-align: center;
    font-weight: 600;
    font-size: 155px;
    line-height: 1;
    letter-spacing: 0;
    color: var(--brand-blue);
    white-space: nowrap;
  }
  .brand-ground {
    position: absolute;
    left: 107px;
    top: 2330px;
    width: 1006px;
    height: 56px;
  }
</style>
</head>
<body>
  <main class="banner">
    <h1 class="tagline">
      <span>Be the</span>
      <span class="tagline-emphasis">Hero</span>
      <span>You’ve been</span>
      <span>waiting for.</span>
    </h1>

    <svg class="brand-emblem" viewBox="0 0 660 660" role="img" aria-label="Kestrel Hub emblem: a caped figure leaping in front of city buildings">
      <defs>
        <radialGradient id="emblemFill" cx="50%" cy="40%" r="60%">
          <stop offset="0%" stop-color="#2a6cb3"/>
          <stop offset="70%" stop-color="#2a6cb3" stop-opacity="0.85"/>
          <stop offset="100%" stop-color="#b84555" stop-opacity="0.7"/>
        </radialGradient>
      </defs>
      <circle cx="330" cy="330" r="330" fill="url(#emblemFill)"/>
    </svg>

    <p class="brand-name">KESTREL HUB</p>

    <svg class="brand-ground" viewBox="0 0 1006 56" aria-hidden="true">
      <defs>
        <radialGradient id="groundShadow" cx="50%" cy="50%" r="50%">
          <stop offset="0%" stop-color="#041426" stop-opacity="0.6"/>
          <stop offset="100%" stop-color="#041426" stop-opacity="0"/>
        </radialGradient>
      </defs>
      <ellipse cx="503" cy="28" rx="503" ry="24" fill="url(#groundShadow)"/>
    </svg>
  </main>
</body>
</html>
```